Rack Card - Digital Marketing Course

I need a double sided rack card designed for a Digital Marketing Course I teach. http://www.tallpinestudio.ca/training is where the course details are.

Digital

```html
<!DOCTYPE html>
<html lang="en">
<head>
<meta charset="utf-8">
<title>Tall Pine Studio – Digital Growth 360 Rack Card</title>
<link rel="stylesheet" href="https://fonts.googleapis.com/css2?family=EB+Garamond:wght@400&family=Montserrat:wght@400;800&display=swap">
<style>
  :root {
    --brand-blue: #1f7ae0;
    --ink-navy: #1b2a6b;
    --paper: #ffffff;
    --headline: #ececec;
    --photo-dark: #161616;
    --photo-mid: #3a3a3a;
  }
  * { margin: 0; padding: 0; box-sizing: border-box; }
  html, body { width: 1200px; height: 2616px; overflow: hidden; background: var(--paper); }
  .rack-card { position: relative; width: 1200px; height: 2616px; background: var(--paper); overflow: hidden; }

  .brand-band { position: absolute; left: 0; top: 0; width: 1200px; height: 258px; background: var(--paper); }
  .brand-square { position: absolute; left: 17px; top: 9px; width: 257px; height: 249px; background: var(--brand-blue); }
  .brand-name {
    position: absolute; left: 318px; top: 26px; width: 870px;
    font-family: 'Montserrat', sans-serif; font-weight: 400; color: var(--brand-blue);
    white-space: nowrap;
  }
  .brand-name .brand-title { display: block; font-size: 124px; line-height: 130px; letter-spacing: 2px; }
  .brand-name .brand-sub { display: block; font-size: 44px; line-height: 60px; letter-spacing: 44px; margin-top: 14px; padding-left: 6px; }

  .hero {
    position: absolute; left: 0; top: 258px; width: 1200px; height: 2123px;
    background:
      linear-gradient(180deg, var(--photo-dark) 0%, #2b2b2b 22%, var(--photo-mid) 45%, #2a2a2a 70%, var(--photo-dark) 100%);
  }
  .headline { position: absolute; left: 0; top: 258px; width: 1200px; height: 2123px; }
  .headline-line {
    position: absolute; left: 0; width: 1200px; text-align: center;
    font-family: 'EB Garamond', serif; font-weight: 400; font-size: 250px; line-height: 1;
    color: var(--headline); white-space: nowrap;
    text-shadow: 0 2px 6px rgba(0,0,0,0.45);
  }
  .line-1 { top: 240px; }
  .line-2 { top: 560px; }
  .line-3 { top: 880px; }
  .line-4 { top: 1195px; }
  .line-5 { top: 1520px; }

  .course-band { position: absolute; left: 0; top: 2381px; width: 1200px; height: 235px; background: var(--paper); border-top: 4px solid var(--brand-blue); }
  .course-name {
    position: absolute; left: 17px; top: 34px; width: 1170px; height: 170px;
    font-family: 'Montserrat', sans-serif; font-weight: 800; color: var(--ink-navy);
  }
  .course-words { position: absolute; left: 0; top: 6px; font-size: 78px; line-height: 80px; }
  .course-number { position: absolute; right: 0; top: -30px; font-size: 220px; line-height: 220px; letter-spacing: -4px; }
</style>
</head>
<body>
<main class="rack-card">
  <header class="brand-band">
    <div class="brand-square" aria-hidden="true"></div>
    <div class="brand-name">
      <span class="brand-title">TALL PINE</span>
      <span class="brand-sub">STUDIO</span>
    </div>
  </header>

  <div class="hero" role="img" aria-label="Dark monochrome photograph of a modern building entrance with glass doors and a staircase at night"></div>

  <h1 class="headline">
    <span class="headline-line line-1">enhance</span>
    <span class="headline-line line-2">your</span>
    <span class="headline-line line-3">teams</span>
    <span class="headline-line line-4">marketing</span>
    <span class="headline-line line-5">skills</span>
  </h1>

  <footer class="course-band">
    <div class="course-name">
      <div class="course-words">DIGITAL<br>GROWTH</div>
      <div class="course-number">360</div>
    </div>
  </footer>
</main>
</body>
</html>
```